Google Form Graphic to suit our Brand and industry

Create a graphic / image for us to put at the top of our client enquiry google form.
The image will be a section of an architectural home with our branding over the top. Preferably translucent.
The image must suit the shape of the google forms image, which is an elongated rectangle
#003d5d - brand colour

Target Market(s)

residential home owners, high end architectural homes

Industry/Entity Type

Residential construction

Colors
0054AA
0677BA
7BADD7
CADEEF
E8F1F8

Requirements
Must have
• our branding and a photo of an architectural home in the background

```html
<!DOCTYPE html>
<html lang="en">
<head>
<meta charset="utf-8">
<title>Form Header Banner Options</title>
<link rel="stylesheet" href="https://fonts.googleapis.com/css2?family=Poppins:wght@300;400;500&display=swap">
<style>
  :root {
    --page-bg: #ffffff;
    --label-ink: #1a1a1a;
    --brand-deep: #003d5d;
    --brand-blue: #0054AA;
    --brand-mid: #0677BA;
    --sky: #a9c8d6;
    --facade: #d6d7d4;
    --glass: #7fa6a8;
    --foliage: #5d6a3c;
    --foliage-dark: #34462e;
    --ink-light: #ffffff;
  }
  html, body {
    margin: 0;
    padding: 0;
    width: 1200px;
    height: 1114px;
    overflow: hidden;
    background: var(--page-bg);
  }
  .sheet {
    position: relative;
    width: 1200px;
    height: 1114px;
  }
  .option-label {
    position: absolute;
    left: 197px;
    margin: 0;
    font-family: 'Poppins', sans-serif;
    font-weight: 400;
    font-size: 11px;
    letter-spacing: 4px;
    color: var(--label-ink);
    line-height: 1;
  }
  .banner {
    position: absolute;
    left: 198px;
    width: 817px;
    display: block;
  }
  .banner-a { top: 115px; height: 211px; }
  .banner-b { top: 471px; height: 206px; }
  .banner-c { top: 831px; height: 206px; }
  .label-a { top: 88px; }
  .label-b { top: 445px; }
  .label-c { top: 802px; }
  .brand-name {
    font-family: 'Poppins', sans-serif;
    font-weight: 400;
    fill: var(--ink-light);
  }
</style>
</head>
<body>
<main class="sheet">

  <svg width="0" height="0" style="position:absolute" aria-hidden="true">
    <defs>
      <linearGradient id="house-photo" x1="0" y1="0" x2="0" y2="1">
        <stop offset="0" stop-color="var(--sky)"/>
        <stop offset="0.22" stop-color="var(--facade)"/>
        <stop offset="0.5" stop-color="var(--glass)"/>
        <stop offset="0.72" stop-color="var(--facade)"/>
        <stop offset="1" stop-color="var(--foliage)"/>
      </linearGradient>
      <linearGradient id="house-side" x1="0" y1="0" x2="1" y2="0">
        <stop offset="0" stop-color="var(--foliage-dark)" stop-opacity="0.7"/>
        <stop offset="0.2" stop-color="var(--foliage-dark)" stop-opacity="0"/>
        <stop offset="0.82" stop-color="var(--foliage)" stop-opacity="0"/>
        <stop offset="1" stop-color="var(--foliage)" stop-opacity="0.8"/>
      </linearGradient>
    </defs>
  </svg>

  <p class="option-label label-a">OPTIONS A</p>
  <svg class="banner banner-a" viewBox="0 0 1191 308" preserveAspectRatio="none">
    <g role="img" aria-label="Photo of a modern architectural home with glass walls among trees">
      <rect width="1191" height="308" fill="url(#house-photo)"/>
      <rect width="1191" height="308" fill="url(#house-side)"/>
    </g>
    <path class="brand-overlay" d="M0 0 H387 C330 60 290 110 275 150 C290 200 340 260 395 308 H0 Z" fill="var(--brand-blue)" opacity="0.72"/>
    <text class="brand-name" x="140" y="168" font-size="36" letter-spacing="12">VELA BUILDWORKS</text>
  </svg>

  <p class="option-label label-b">OPTIONS B</p>
  <svg class="banner banner-b" viewBox="0 0 1191 301" preserveAspectRatio="none">
    <g role="img" aria-label="Photo of a modern architectural home with glass walls among trees">
      <rect width="1191" height="301" fill="url(#house-photo)"/>
      <rect width="1191" height="301" fill="url(#house-side)"/>
    </g>
    <path class="brand-overlay" d="M0 0 H507 C460 60 410 110 395 150 C420 200 460 250 507 301 H0 Z" fill="var(--brand-blue)" opacity="0.72"/>
    <text class="brand-name" x="174" y="172" font-size="52" letter-spacing="16">VELA BUILDWORKS</text>
  </svg>

  <p class="option-label label-c">OPTIONS C</p>
  <svg class="banner banner-c" viewBox="0 0 1191 301" preserveAspectRatio="none">
    <g role="img" aria-label="Photo of a modern architectural home with glass walls among trees">
      <rect width="1191" height="301" fill="url(#house-photo)"/>
      <rect width="1191" height="301" fill="url(#house-side)"/>
    </g>
    <path class="brand-overlay" d="M0 0 H557 C510 60 470 105 455 150 C480 205 520 255 562 301 H0 Z" fill="var(--brand-blue)" opacity="0.72"/>
    <text class="brand-name" x="177" y="178" font-size="66" letter-spacing="20">VELA BUILDWORKS</text>
  </svg>

</main>
</body>
</html>
```